OLVRA Web Design (Need help to re-design our website)

We need someone to help us re-design our website and launch it. All contents for the website are ready. (https://olvra-example.com.au/)

-Rearrange categories:
1. Heating & Cooling
2. Remove Home Appliance
3. Remove Entertainment

Home page - redesign (It will be a nice touch if the banner is in the loop).

NOTE:
-Brand colour blue and orange.
-Try using professional fonts (Example: Helvetica, etc.)
-The website's Footer should be readable and use light colour.

Target Market(s)

Residentials & commercial buildings

Industry/Entity Type

Heat Ventilation and Cooling Industry, Technology , Renewables

Coding

Coded - Design and coding required

Colors
0094D4
00A9DD
6FCCEA
C7EBF8
E9F6FB
59FF00
82FF00
B8FF75
E3FFCB
F4FFEA
F0912C
F2A743
F7CA91
FBE8D2
FDF5EE

Requirements
Nice to have
• Effects/transition on the words/copy/images.

```html
<!DOCTYPE html>
<html lang="en">
<head>
<meta charset="utf-8">
<title>OLVRA – Heating &amp; Cooling</title>
<link rel="stylesheet" href="https://fonts.googleapis.com/css2?family=Montserrat:wght@400;500;600;700;800&family=Arimo:wght@400;700&display=swap">
<style>
:root{
  --blue:#1262b3;
  --blue-dark:#0e56a0;
  --orange:#f5912b;
  --orange-soft:#fdebd6;
  --blue-soft:#e3ecf6;
  --ink:#222;
  --muted:#444;
  --white:#fff;
  --grey-line:#ddd;
}
*{box-sizing:border-box;margin:0;padding:0}
html,body{width:1200px;height:4396px;overflow:hidden}
body{position:relative;font-family:"Montserrat",sans-serif;color:var(--ink);background:var(--white)}
.abs{position:absolute}
a{color:inherit;text-decoration:none}

/* Header */
.site-header{left:0;top:0;width:1200px;height:133px;background:var(--white)}
.brand{display:flex;align-items:center;gap:14px;font-family:"Montserrat",sans-serif;font-weight:700;color:var(--blue);letter-spacing:4px}
.brand-mark{width:44px;height:44px;background:var(--orange);border-radius:50%}
.site-header .brand{left:77px;top:48px;font-size:46px}
.social-row{left:616px;top:39px;display:flex;gap:6px}
.social-dot{width:18px;height:18px;border-radius:4px;background:var(--blue)}
.search{left:674px;top:31px;width:214px;height:37px;border:1.5px solid #bbb;border-radius:20px;font-size:12px;color:#999;padding:10px 16px}
.search svg{position:absolute;right:12px;top:10px}
.btn-book{left:901px;top:31px;width:226px;height:37px;background:var(--blue);color:var(--white);font-size:13px;font-weight:500;display:flex;align-items:center;justify-content:center;border-radius:20px 20px 20px 0}
.main-nav{left:604px;top:86px;display:flex;gap:32px;font-size:12.5px;font-weight:500;color:#333}
.main-nav .active{color:var(--orange);border-bottom:2px solid var(--orange);padding-bottom:8px}

/* Hero */
.hero{left:0;top:133px;width:1200px;height:661px;overflow:hidden}
.hero-photo{position:absolute;inset:0;background:linear-gradient(100deg,#d9d7d4 0%,#c9c6c2 45%,#b8b4ae 70%,#dedcd9 100%)}
.hero-shape{position:absolute;left:0;top:0}
.hero-kicker{left:77px;top:180px;font-size:38px;font-weight:600;color:var(--blue)}
.hero-title{left:77px;top:232px;font-size:66px;line-height:76px;font-weight:800;color:var(--white)}
.hero-sub{left:77px;top:398px;font-size:37px;font-weight:500;color:var(--white)}
.btn-explore{left:80px;top:473px;width:256px;height:65px;background:var(--blue);color:var(--white);font-size:21px;font-weight:500;display:flex;align-items:center;justify-content:center;border-radius:40px 40px 0 40px}
.hero-dots{left:394px;top:571px;display:flex;gap:5px}
.hero-dots span{width:11px;height:11px;border-radius:50%;background:#e6c8a4}
.hero-dots span:first-child{background:var(--white)}

/* Features */
.feature{top:867px;height:150px;display:flex;align-items:flex-start;padding:34px 18px 0 20px;gap:16px;color:var(--white);box-shadow:0 3px 8px rgba(0,0,0,.18)}
.feature.blue{background:var(--blue)}
.feature.orange{background:var(--orange)}
.feature-icon{flex:0 0 78px;height:78px;border-radius:50%;display:flex;align-items:center;justify-content:center;margin-top:4px}
.feature.blue .feature-icon{background:var(--orange)}
.feature.orange .feature-icon{background:var(--blue)}
.feature h3{font-size:16px;font-weight:700;margin:0 0 8px}
.feature p{font-size:12.5px;line-height:18px}

/* Section headings */
.section-title{display:flex;align-items:center;gap:20px;font-family:"Arimo",sans-serif;font-weight:700;color:var(--blue);font-size:56px;white-space:nowrap}
.title-mark{width:36px;height:36px;background:var(--orange);border-radius:50%}

/* Product cards */
.card{width:502px;height:558px;background:var(--white);box-shadow:0 2px 10px rgba(0,0,0,.18);text-align:center}
.card-media{height:337px;position:relative;overflow:hidden}
.card-media .arc{position:absolute;right:0;top:60px;width:280px;height:277px;border-top-left-radius:280px}
.card-media .product{position:absolute;left:50%;top:40px;transform:translateX(-50%);border-radius:8px}
.card h3{font-family:"Montserrat",sans-serif;font-size:21px;font-weight:600;margin-top:30px}
.card p{font-size:13.5px;line-height:22.5px;color:var(--muted);width:400px;margin:12px auto 0}
.card .more{display:inline-flex;align-items:center;gap:8px;font-size:12.5px;font-weight:500;margin-top:16px}
.card.is-blue h3,.card.is-blue .more{color:var(--blue)}
.card.is-orange h3,.card.is-orange .more{color:var(--orange)}

/* About */
.about{left:0;top:2577px;width:1200px;height:632px;background:var(--blue)}
.about-media{left:218px;top:125px;width:303px;height:384px;background:linear-gradient(160deg,#f2f2f2,#b9bcc0 55%,#e5e6e8);border-radius:180px 0 180px 0}
.about-mark{left:776px;top:110px;width:40px;height:40px;border-radius:50%;background:var(--orange)}
.about h2{left:611px;top:160px;width:370px;text-align:center;color:var(--white);font-size:50px;font-weight:600}
.about p{left:611px;top:247px;width:370px;color:var(--white);font-size:13.5px;line-height:27px;text-align:justify;text-align-last:center}
.btn-readmore{left:667px;top:446px;width:257px;height:63px;background:var(--orange);color:var(--white);font-size:21px;font-weight:500;display:flex;align-items:center;justify-content:center;border-radius:40px 40px 0 40px}

/* Benefits */
.benefit{top:3462px;width:220px;text-align:center}
.benefit-icon{width:120px;height:120px;margin:0 auto;border-radius:50%;background:var(--blue);border:6px solid var(--orange);display:flex;align-items:center;justify-content:center}
.benefit h4{font-size:18px;font-weight:600;margin-top:22px;color:#111}

/* Savings band */
.savings{left:0;top:3721px;width:1200px;height:427px;background:var(--orange);text-align:center}
.savings .kicker{left:0;width:1200px;top:92px;font-size:40px;font-weight:600;color:var(--blue)}
.savings .big{left:0;width:1200px;top:150px;font-size:88px;font-weight:800;color:var(--white);letter-spacing:1px}
.btn-contact{left:473px;top:279px;width:256px;height:65px;background:var(--blue);color:var(--white);font-size:21px;font-weight:500;display:flex;align-items:center;justify-content:center;border-radius:40px 40px 0 40px}

/* Footer */
.site-footer{left:0;top:4148px;width:1200px;height:196px;background:var(--blue);color:var(--white)}
.site-footer .brand{left:77px;top:84px;font-size:40px;color:var(--white)}
.site-footer .brand-mark{width:38px;height:38px}
.footer-nav{left:332px;top:110px;display:flex;gap:32px;font-size:12.5px;font-weight:500}
.newsletter-label{left:832px;top:60px;font-size:16px;font-weight:500}
.newsletter{left:823px;top:90px;width:304px;height:46px;border:2px solid var(--orange);background:var(--orange);display:flex;align-items:center;padding-left:16px;font-size:11.5px}
.newsletter .signup{margin-left:auto;margin-right:4px;background:var(--blue);height:34px;width:90px;display:flex;align-items:center;justify-content:center;font-size:13px;border-radius:4px}
.bottom-bar{left:0;top:4344px;width:1200px;height:52px;background:var(--white);display:flex;align-items:center;padding:0 78px;font-size:12px;color:#333}
.bottom-bar .social{margin-left:auto;display:flex;gap:8px}
.bottom-bar .social span{width:28px;height:28px;border-radius:50%;background:var(--blue)}
</style>
</head>
<body>

<header class="site-header abs">
  <div class="brand abs"><span class="brand-mark"></span>OLVRA</div>
  <div class="social-row abs"><span class="social-dot"></span><span class="social-dot"></span></div>
  <div class="search abs">Search...
    <svg width="16" height="16" viewBox="0 0 16 16"><circle cx="7" cy="7" r="5" fill="none" stroke="#999" stroke-width="1.5"/><line x1="11" y1="11" x2="15" y2="15" stroke="#999" stroke-width="1.5"/></svg>
  </div>
  <a class="btn-book abs" href="#">Book Appointment</a>
  <nav class="main-nav abs">
    <a class="active" href="#">HOME</a><a href="#">OUR STORY</a><a href="#">HEATING &amp; COOLING ▾</a><a href="#">SUPPORT</a><a href="#">CONTACT US</a>
  </nav>
</header>

<section class="hero abs">
  <div class="hero-photo" role="img" aria-label="Bright living room with a wall-mounted split air conditioner, pendant lamps and a sofa"></div>
  <svg class="hero-shape" width="1200" height="661" viewBox="0 0 1200 661">
    <path d="M0,0 L300,0 C560,160 770,430 830,661 L0,661 Z" fill="#f5912b" opacity=".9"/>
  </svg>
  <div class="hero-kicker abs">Revolutionise</div>
  <h1 class="hero-title abs">HEATING &amp;<br>COOLING</h1>
  <div class="hero-sub abs">Industry Australiawide</div>
  <a class="btn-explore abs" href="#">EXPLORE</a>
  <div class="hero-dots abs"><span></span><span></span><span></span></div>
</section>

<svg width="0" height="0" style="position:absolute">
  <symbol id="truck" viewBox="0 0 44 28"><rect x="1" y="4" width="26" height="16" rx="2" fill="#fff"/><path d="M27 9h9l6 6v5H27z" fill="#fff"/><circle cx="9" cy="22" r="4" fill="#fff" stroke="currentColor" stroke-width="2"/><circle cx="34" cy="22" r="4" fill="#fff" stroke="currentColor" stroke-width="2"/></symbol>
  <symbol id="arrow" viewBox="0 0 18 10"><path d="M0 5h15M11 1l5 4-5 4" fill="none" stroke="currentColor" stroke-width="2"/></symbol>
</svg>

<div class="feature blue abs" style="left:82px;width:323px">
  <div class="feature-icon" style="color:#f5912b"><svg width="44" height="28"><use href="#truck"/></svg></div>
  <div><h3>QUALITY PRODUCTS</h3><p>We only offer high-quality products that are built to last.</p></div>
</div>
<div class="feature orange abs" style="left:434px;width:334px">
  <div class="feature-icon" style="color:#1262b3"><svg width="44" height="28"><use href="#truck"/></svg></div>
  <div><h3>EXPERT INSTALLATION</h3><p>Our team of experienced professionals will ensure that your heat pump water heater</p></div>
</div>
<div class="feature blue abs" style="left:795px;width:323px">
  <div class="feature-icon" style="color:#f5912b"><svg width="44" height="28"><use href="#truck"/></svg></div>
  <div><h3>CUSTOMER SERVICE</h3><p>We pride ourselves on our excellent customer service and are always here</p></div>
</div>

<h2 class="section-title abs" style="left:330px;top:1144px"><span class="title-mark"></span>Heating &amp; Cooling</h2>

<article class="card is-blue abs" style="left:77px;top:1302px">
  <div class="card-media"><div class="arc" style="background:var(--blue-soft)"></div>
    <div class="product" role="img" aria-label="Two white heat pump water heater cylinders" style="width:260px;height:280px;background:linear-gradient(90deg,#e9e9e9,#fafafa,#d5d5d5)"></div></div>
  <h3>Heat Pump</h3>
  <p>Our heat pump water heater works by extracting heat from the surrounding air and using it to heat the water. It operates similarly to an air conditioner, but in reverse.</p>
  <a class="more" href="#">READ MORE <svg width="18" height="10"><use href="#arrow"/></svg></a>
</article>
<article class="card is-orange abs" style="left:616px;top:1302px">
  <div class="card-media"><div class="arc" style="background:var(--orange-soft)"></div>
    <div class="product" role="img" aria-label="White wall-mounted split air conditioner" style="top:115px;width:380px;height:95px;background:linear-gradient(180deg,#fafafa,#dedede)"></div></div>
  <h3>Air Conditioners</h3>
  <p style="margin-top:22px">OLVRA Air Conditioners, a product in development that promises to be one of the best energy-efficient solutions on the market.</p>
  <a class="more" href="#" style="margin-top:26px">READ MORE <svg width="18" height="10"><use href="#arrow"/></svg></a>
</article>
<article class="card is-orange abs" style="left:77px;top:1898px">
  <div class="card-media"><div class="arc" style="background:var(--orange-soft)"></div>
    <div class="product" role="img" aria-label="Grey swimming pool heat pump unit with a round fan" style="top:58px;width:290px;height:240px;background:linear-gradient(160deg,#d9dde2,#a9afb6)"></div></div>
  <h3>Swimming Pool Heat Pump</h3>
  <p>OLVRA Swimming Pool Heat Pump is currently in development and aims to be one of the most energy-efficient solutions for heating your swimming pool.</p>
  <a class="more" href="#">READ MORE <svg width="18" height="10"><use href="#arrow"/></svg></a>
</article>
<article class="card is-blue abs" style="left:616px;top:1898px">
  <div class="card-media"><div class="arc" style="background:var(--blue-soft)"></div>
    <div class="product" role="img" aria-label="White monoblock heat pump outdoor unit with a round fan" style="top:60px;width:290px;height:230px;background:linear-gradient(160deg,#f3f3f3,#c6c8ca)"></div></div>
  <h3>Monoblock Heat Pump</h3>
  <p>OLVRA Monoblock Heat Pump is an upcoming product that promises to revolutionize the heating and cooling industry with its exceptional energy efficiency.</p>
  <a class="more" href="#">READ MORE <svg width="18" height="10"><use href="#arrow"/></svg></a>
</article>

<section class="about abs">
  <div class="about-media abs" role="img" aria-label="Collage of air conditioner and heat pump fan close-ups"></div>
  <div class="about-mark abs"></div>
  <h2 class="abs">About Olvra</h2>
  <p class="abs">OLVRA is a company dedicated to manufacturing and installing energy-efficient products that reduce energy consumption, save costs, and promote sustainability. Our mission is to help individuals and businesses reduce their carbon footprint while also enhancing their comfort and quality of life.</p>
  <a class="btn-readmore abs" href="#">READ MORE</a>
</section>

<h2 class="section-title abs" style="left:175px;top:3332px"><span class="title-mark"></span>Benefits of OLVRA Heat Pump</h2>

<div class="benefit abs" style="left:150px">
  <div class="benefit-icon"><svg width="60" height="60" viewBox="0 0 60 60" fill="none" stroke="#fff" stroke-width="3"><circle cx="30" cy="30" r="20"/><circle cx="30" cy="30" r="8"/><path d="M30 30l6-6"/></svg></div>
  <h4>Energy Efficient</h4>
</div>
<div class="benefit abs" style="left:370px">
  <div class="benefit-icon"><svg width="60" height="60" viewBox="0 0 60 60" fill="none" stroke="#fff" stroke-width="3"><path d="M30 10c12 6 14 18 0 28C16 28 18 16 30 10z"/><path d="M30 20v30M10 44c8 0 14 6 20 6s12-6 20-6"/></svg></div>
  <h4>Eco-Friendly</h4>
</div>
<div class="benefit abs" style="left:586px">
  <div class="benefit-icon"><svg width="60" height="60" viewBox="0 0 60 60" fill="none" stroke="#fff" stroke-width="3"><circle cx="30" cy="30" r="20"/><path d="M36 22c-2-3-12-3-12 3s12 4 12 10-10 6-13 2M30 16v28"/></svg></div>
  <h4>Cost-Effective</h4>
</div>
<div class="benefit abs" style="left:817px">
  <div class="benefit-icon"><svg width="60" height="60" viewBox="0 0 60 60" fill="none" stroke="#fff" stroke-width="3"><path d="M30 8l18 7v13c0 12-8 20-18 24-10-4-18-12-18-24V15z"/><path d="M21 30l7 7 12-13"/></svg></div>
  <h4>Low Maintenance</h4>
</div>

<section class="savings abs">
  <div class="kicker abs">Save Upto</div>
  <div class="big abs">75% ELECTRICITY COST</div>
  <a class="btn-contact abs" href="#">CONTACT US</a>
</section>

<footer class="site-footer abs">
  <div class="brand abs"><span class="brand-mark"></span>OLVRA</div>
  <nav class="footer-nav abs"><a href="#">OUR STORY</a><a href="#">HEATING &amp; COOLING</a><a href="#">SUPPORT</a><a href="#">CONTACT US</a></nav>
  <div class="newsletter-label abs">Join Our Newsletter</div>
  <div class="newsletter abs">Enter Your Email Address<span class="signup">Sign Up</span></div>
</footer>
<div class="bottom-bar abs">© Copyright 2024 OLVRA - All rights reserved.
  <div class="social"><span></span><span></span><span></span></div>
</div>

</body>
</html>
```